Flyer-Design für Konzertflyer gemischter Chor
Zielgruppe
Wir, die Klangfreunde Wellbach sind ein gemischter Chor aus der Schweiz. Für unser nächstes Konzert mit dem Titel ' Lieder zum Träumen' brauchen wir einen Flyer der auf den Anlass Aufmerksam macht.
Näheres zum Chor auf unserer Website www.klangfreunde-wellbach.ch.
Aufgabenstellung
Mit dem Titel sind nicht nur Lieder zum verlieben gemeint sondern auch Songs in die man sich verlieben kann oder die einem an etwas schönes Erinnern. Wir denken da an ein stimmungsvolles Design mit nicht nur roten Herzen.
Programmausschnitt: Winds across the silver bay , Harlan Moody / Lanterns in the rain / Kima Soro / Walk beside the quiet river tonight, Garth Wells / Paper boats at dusk, Russ Tanner / Tidal hymn, Trevor Halloway / Brightwater, Harbor lane tales / Bells over meadows , Cedar hall
Format: A5 hochkant.
Text: "Lieder zum Träumen" Konzert Klangfreunde Wellbach.
Samstag 19. November 17.00 Uhr, Wellbach/Lindmatt, Singsaal Lindenhain
Sonntag 20. November 17.00Uhr, Rosental am See, Kornblumsaal
Eintritt frei Kollekte
www.klangfreunde-wellbach.ch

```html
<!DOCTYPE html>
<html lang="de">
<head>
<meta charset="utf-8">
<title>Lieder zum Träumen – Konzert Klangfreunde Wellbach</title>
<link rel="stylesheet" href="https://fonts.googleapis.com/css2?family=Exo+2:ital,wght@1,800;1,900&family=Barlow:wght@500;600;700&display=swap">
<style>
  :root {
    --page-bg: #e6e6e6;
    --magenta: #a5137f;
    --white: #ffffff;
    --accent-red: #d32a2c;
    --ink: #2a1a25;
    --photo-light: #d8cdb4;
    --photo-mid: #a8977a;
    --photo-dark: #3a3024;
  }
  * { box-sizing: border-box; margin: 0; padding: 0; }
  html, body {
    width: 1200px; height: 1200px; overflow: hidden;
    background: var(--page-bg);
  }
  .flyer {
    position: absolute; left: 220px; top: 50px;
    width: 760px; height: 1100px;
    background: var(--magenta);
    color: var(--white);
    font-family: "Barlow", sans-serif;
    overflow: hidden;
  }
  .headline {
    position: absolute;
    font-family: "Exo 2", sans-serif;
    font-weight: 900; font-style: italic;
    line-height: 1.1; letter-spacing: -1px;
    white-space: nowrap;
  }
  .headline--top { left: 60px; top: 24px; font-size: 104px; }
  .headline--bottom { left: 150px; top: 134px; font-size: 104px; }
  .headline--small {
    left: 64px; top: 198px; font-size: 34px; letter-spacing: 0;
  }
  .event-label {
    position: absolute; left: 330px; top: 108px;
    background: var(--accent-red);
    padding: 7px 16px;
    font-weight: 700; font-size: 25px; letter-spacing: 0.3px;
    white-space: nowrap;
    transform: rotate(-3deg);
    box-shadow: 0 2px 4px rgba(0,0,0,0.25);
  }
  .hero-image {
    position: absolute; left: 0; top: 250px;
    width: 760px; height: 435px;
    background: radial-gradient(ellipse at 50% 55%, var(--photo-dark) 0%, var(--photo-mid) 28%, var(--photo-light) 60%, var(--photo-mid) 100%);
  }
  .entry-badge {
    position: absolute; left: 56px; top: 282px;
    width: 128px; height: 128px; border-radius: 50%;
    background: var(--accent-red);
    display: flex; align-items: center; justify-content: center;
    text-align: center;
    font-weight: 700; font-size: 19px; line-height: 1.25;
    transform: rotate(-6deg);
  }
  .schedule {
    position: absolute; left: 0; top: 722px; width: 760px;
    text-align: center;
  }
  .schedule__day {
    font-family: "Exo 2", sans-serif;
    font-style: italic; font-weight: 900;
    font-size: 56px; line-height: 1.05;
    padding-left: 60px;
  }
  .schedule__day .date { font-weight: 800; font-size: 46px; }
  .schedule__detail {
    font-weight: 500; font-size: 23px; line-height: 1.45;
    letter-spacing: 0.3px; padding-left: 70px;
  }
  .schedule__entry + .schedule__entry { margin-top: 28px; }
  .website {
    position: absolute; left: 0; bottom: 42px; width: 760px;
    text-align: center; padding-left: 70px;
    font-weight: 700; font-size: 24px; color: var(--ink);
  }
</style>
</head>
<body>
  <main class="flyer">
    <h1>
      <span class="headline headline--top">LIEDER</span>
      <span class="headline headline--small">ZUM</span>
      <span class="headline headline--bottom">TRÄUMEN</span>
    </h1>
    <div class="event-label">Konzert Klangfreunde Wellbach</div>

    <div class="hero-image" role="img" aria-label="Foto: aufgerollte Notenblätter, die in der Mitte ein Herz formen, in warmen Sepiatönen"></div>

    <div class="entry-badge">Eintritt frei –<br>Kollekte</div>

    <section class="schedule">
      <div class="schedule__entry">
        <p class="schedule__day">SAMSTAG <span class="date">19. NOV. 2016</span></p>
        <p class="schedule__detail">17.00 Uhr · Wellbach/Lindmatt</p>
        <p class="schedule__detail">Singsaal Schulhaus Lindenhain</p>
      </div>
      <div class="schedule__entry">
        <p class="schedule__day">SONNTAG <span class="date">20. NOV. 2016</span></p>
        <p class="schedule__detail">17.00 Uhr · Rosental am See</p>
        <p class="schedule__detail">Kornblumsaal</p>
      </div>
    </section>

    <p class="website">www.klangfreunde-wellbach.ch</p>
  </main>
</body>
</html>
```